Homebuilder & Remodeling Firm looking for archectrual looking website

We are a Custom home building & remodeling company since 1986 and would like to launch a website.Carl Tondevik the principle of the firm is a graduate of Harwell Univesity school of architecture and draws his own designs and working drawings. and has done many residential, single and multi family projects in the Dallas Ft Worth Metroplex. We want our website to be architectural in design and visually appealing. We will eventually have photos to provide for you. The message we want to communicate is we have current update knowledge with trends, and longevity in experience. Our message is that we are a firm that designs and remodels fully through and we provide a well executed custom home that is unique to each client. The Homes that we build are unique ,authentic and sustainable architectural styles such as mid century modern, contemporary, transitional and they are sophisticated homes to compliment individual lifestyles of our clients. We have a passion for construction and an attention to detail that makes your dreams come to life. We listen to each clients every need in functionality and form and take them from pre-construction to post-construction follow -up.
We help you invest in your home. Thoughts Create Reality

EXAMPLES OF WEBSITES THAT WE LIKE. PLEASE DO
MORE CONTEMPORARY, SLEEK, ARCHITECTURAL

* Please make the LOGO a bigger part of design

http://pellamcrew.build/
https://www.vintrasol.co/
http://dostavanehomes.com/
http://www.milesfardowdesign.com/
http://www.quillmerton.com/
http://fennikdesignstudios.com/about
http://brandelorgc.com/

thank you,

Reason: We have many clients asking to see our website and re ready to launch something for them to look at

Target Market(s)

Home owners, home buyers, interior designers, All ages

Industry/Entity Type

Builders

Coding

Coded - Design and coding required

Number of Pages Required

5+ page

Font styles to use
Sans Serif

Requirements
Must have
• HTML5 OR PHP
• graphic artist must speak English:
• *Visually appealing, user friendly,
• * the website should reflect the stability and integrity of the company since it has been in business for over 30 years
• * a sophistication and refinement is our mandate.
Should not have
• Too busy, too much going on, we want more minimal in design and artsitic

```html
<!DOCTYPE html>
<html lang="en">
<head>
<meta charset="utf-8">
<title>Halvern Development — Custom Homes &amp; Remodeling</title>
<link rel="stylesheet" href="https://fonts.googleapis.com/css2?family=Raleway:wght@300;400;500;600&family=Open+Sans:wght@400;600;700&display=swap">
<style>
:root{
  --blue:#0d4fa3;
  --blue-dark:#0a3f86;
  --blue-band:#1557ab;
  --ink:#2b2b2b;
  --muted:#6f6f6f;
  --line:#dcdcdc;
  --white:#ffffff;
  --hero-a:#2a2725;
  --hero-b:#4a4540;
}
*{box-sizing:border-box;margin:0;padding:0}
html,body{width:1200px;height:2985px;overflow:hidden;background:var(--white)}
body{position:relative;font-family:"Open Sans",Arial,sans-serif;color:var(--ink)}
.abs{position:absolute}
h1,h2,h3{font-family:"Raleway",Arial,sans-serif;font-weight:400}

/* hero */
.hero{left:0;top:0;width:1200px;height:600px}
.hero-photo{left:0;top:0;width:1200px;height:560px;background:linear-gradient(180deg,#1d1b1a 0%,var(--hero-b) 45%,#6b635b 70%,#3b3734 100%)}
.hero-curve{left:0;top:440px;width:1200px;height:170px}
.brand{left:98px;top:14px;display:flex;align-items:center;gap:14px;color:var(--white)}
.brand-box{width:46px;height:62px;border:3px solid currentColor}
.brand-name{font-family:"Raleway",Arial,sans-serif;font-size:30px;font-weight:400;line-height:1}
.brand-tag{font-family:"Raleway",Arial,sans-serif;font-size:12px;letter-spacing:5px;margin-top:6px}
.top-contact{right:98px;top:14px;display:flex;gap:30px;color:var(--white);font-size:15px;align-items:center}
.top-contact span{display:flex;align-items:center;gap:12px}
.icon-dot{width:30px;height:30px;border-radius:50%;border:1.5px solid var(--white);display:flex;align-items:center;justify-content:center}
.nav{right:98px;top:58px;display:flex;gap:28px;color:var(--white);font-size:16px;align-items:center}
.nav .active{color:#5aa0ff}
.hero-title{left:0;top:205px;width:1200px;text-align:center;color:var(--white);font-size:74px;font-weight:300;letter-spacing:2px}
.hero-sub{left:0;top:296px;width:1200px;text-align:center;color:var(--white);font-size:21px;font-weight:600}
.hero-btn{left:494px;top:350px;width:212px;height:40px;border:2px solid var(--white);border-radius:20px;color:var(--white);font-size:15px;font-weight:700;display:flex;align-items:center;justify-content:center}
.dots{left:562px;top:504px;display:flex;gap:6px}
.dots i{width:14px;height:14px;border-radius:50%;border:2px solid var(--white)}
.dots i.on{background:#5aa0ff;border-color:#5aa0ff}

/* headings */
.section-title{left:0;width:1200px;text-align:center;font-size:34px;color:var(--ink);font-weight:400}
.lead{left:210px;top:722px;width:780px;text-align:center;font-size:12px;line-height:24px;color:var(--muted)}

/* feature cards */
.card{top:808px;width:316px;height:366px;border:1px solid var(--line);box-shadow:0 2px 6px rgba(0,0,0,.08);background:var(--white)}
.card-photo{left:8px;top:8px;width:298px;height:190px}
.card h3{position:absolute;left:0;top:228px;width:100%;text-align:center;font-size:20px;color:var(--ink)}
.card p{position:absolute;left:40px;top:268px;width:236px;text-align:center;font-size:12px;line-height:22px;color:var(--muted)}
.more{font-size:12px;font-weight:700;color:var(--blue)}
.card .more{position:absolute;left:0;top:326px;width:100%;text-align:center}

/* services */
.services{left:0;top:1246px;width:1200px;height:540px}
.svc{top:1366px;width:240px;text-align:center;color:var(--white)}
.svc-ring{width:180px;height:180px;border-radius:50%;border:1.5px solid rgba(255,255,255,.85);margin:0 auto;display:flex;align-items:center;justify-content:center}
.svc h3{font-size:20px;margin-top:28px;font-weight:400}
.svc p{font-size:12px;line-height:22px;margin:10px auto 0;width:220px}
.svc .more{color:var(--white);display:block;margin-top:10px}

/* blog */
.post{top:1876px;width:324px}
.post-photo{width:324px;height:214px;border:1px solid var(--line)}
.date{left:-6px;top:140px;width:46px;height:64px;background:var(--blue);color:var(--white);text-align:center;padding-top:6px}
.date b{display:block;font-size:22px;line-height:26px}
.date small{font-size:11px}
.post h3{font-family:"Open Sans",Arial,sans-serif;font-weight:700;font-size:19px;margin-top:28px}
.post p{font-size:12px;line-height:22px;color:var(--muted);margin-top:10px;width:316px}
.meta{margin-top:18px;border-top:1px solid var(--line);padding-top:12px;font-size:11px;color:var(--muted);display:flex;gap:22px}
.meta span{display:flex;gap:6px;align-items:center}
.rule{left:98px;top:2294px;width:1012px;height:1px;background:var(--line)}

/* gallery */
.gallery{left:0;top:2420px;width:1200px;height:244px;display:flex;gap:4px}
.gallery div{flex:1}
.arrow{top:2520px;width:20px;height:44px;background:rgba(0,0,0,.35);display:flex;align-items:center;justify-content:center}

/* footer */
.foot-brand{left:90px;top:2768px;display:flex;align-items:center;gap:12px;color:var(--blue-dark)}
.foot-brand .brand-box{width:36px;height:50px}
.foot-brand .brand-name{font-size:26px}
.foot-brand .brand-tag{font-size:10px;letter-spacing:4px;color:#8a8a8a}
.foot-col{top:2718px}
.foot-col h4{font-family:"Raleway",Arial,sans-serif;font-weight:500;font-size:17px;margin-bottom:18px}
.foot-col li{list-style:none;font-size:12px;color:var(--muted);line-height:24px}
.foot-col p{font-size:12px;color:var(--muted);line-height:20px}
.field{margin-top:18px;width:244px;border-bottom:1px solid var(--line);font-size:11px;color:#aaa;padding:0 0 8px 12px}
.sub-btn{margin-top:16px;width:96px;height:34px;border:1px solid var(--blue);border-radius:17px;color:var(--blue);font-size:11px;font-weight:700;display:flex;align-items:center;justify-content:center}
.c-row{display:flex;gap:20px;font-size:12px;color:var(--muted);line-height:20px;margin-bottom:22px}
.foot-rule{left:98px;top:2928px;width:1012px;height:1px;background:var(--line)}
.copy{left:98px;top:2952px;font-size:12px;color:var(--muted)}
.social{top:2946px;width:30px;height:30px;border-radius:50%;border:1px solid var(--line)}
</style>
</head>
<body>

<section class="hero abs">
  <div class="hero-photo abs" role="img" aria-label="Modern dark kitchen interior with island and warm lamps"></div>
  <svg class="hero-curve abs" viewBox="0 0 1200 170" preserveAspectRatio="none">
    <path d="M0 60 Q600 140 1200 60 L1200 170 L0 170 Z" fill="#fff"/>
    <path d="M20 92 Q600 210 1180 92 Q600 170 20 92 Z" fill="#0d4fa3"/>
  </svg>
  <div class="brand abs">
    <div class="brand-box"></div>
    <div><div class="brand-name">Halvern Development</div><div class="brand-tag">CUSTOM HOMES • REMODELING</div></div>
  </div>
  <div class="top-contact abs">
    <span><i class="icon-dot"><svg width="14" height="14" viewBox="0 0 24 24"><path d="M6 2l4 4-2 3c1 3 4 6 7 7l3-2 4 4-3 4C10 22 2 14 2 5z" fill="#fff"/></svg></i>1 888 888 8888</span>
    <span><i class="icon-dot"><svg width="14" height="12" viewBox="0 0 24 18"><rect x="1" y="1" width="22" height="16" fill="none" stroke="#fff" stroke-width="2"/><path d="M1 1l11 9 11-9" fill="none" stroke="#fff" stroke-width="2"/></svg></i>info@halverndevelopment.com</span>
  </div>
  <nav class="nav abs">
    <span class="active">Home</span><span>About us</span><span>Services</span><span>Gallery</span><span>Blog</span><span>Contact us</span>
    <svg width="16" height="16" viewBox="0 0 24 24"><circle cx="10" cy="10" r="7" fill="none" stroke="#fff" stroke-width="3"/><path d="M15 15l7 7" stroke="#fff" stroke-width="3"/></svg>
  </nav>
  <h1 class="hero-title abs">HALVERN DEVELOPMENT</h1>
  <div class="hero-sub abs">We are a Custom home building &amp; remodeling company since 1986</div>
  <div class="hero-btn abs">REQUEST A QUOTE</div>
  <div class="dots abs"><i class="on"></i><i></i><i></i><i></i></div>
</section>

<h2 class="section-title abs" style="top:662px">WELCOME TO HALVERN DEVELOPMENT</h2>
<p class="lead abs">At vero eos et accusamus et iusto odio dignissimos ducimus qui blanditiis praesentium voluptatum deleniti atque corrupti quos dolores et quas molestias excepturi sint occaecati cupiditate non p idique sunt in culpa qui officia deserunt mollitia animi, id est</p>

<article class="card abs" style="left:98px">
  <div class="card-photo abs" role="img" aria-label="Architectural sketch of a modern white house" style="background:linear-gradient(160deg,#f4f6f8 0%,#cfdff0 55%,#3f7fd0 100%)"></div>
  <svg class="abs" style="left:8px;top:160px" width="298" height="40" viewBox="0 0 298 40" preserveAspectRatio="none"><path d="M0 0 Q149 50 298 0 L298 40 L0 40Z" fill="#fff"/><path d="M0 6 Q149 54 298 6 Q149 42 0 6Z" fill="#0d4fa3"/></svg>
  <h3>EXCELLENT DESIGN</h3>
  <p>Nam libero tempore, cum soluta nobis est teli gendi optio cumque nihil impedit quo</p>
  <span class="more">READ MORE &gt;&gt;</span>
</article>
<article class="card abs" style="left:444px">
  <div class="card-photo abs" role="img" aria-label="Modern home with pool at dusk" style="background:linear-gradient(180deg,#6fa6e0 0%,#9fb8c8 40%,#3d6a5a 70%,#3aa0b8 100%)"></div>
  <svg class="abs" style="left:8px;top:160px" width="298" height="40" viewBox="0 0 298 40" preserveAspectRatio="none"><path d="M0 0 Q149 50 298 0 L298 40 L0 40Z" fill="#fff"/><path d="M0 6 Q149 54 298 6 Q149 42 0 6Z" fill="#0d4fa3"/></svg>
  <h3>REMODELING</h3>
  <p>Nam libero tempore, cum soluta nobis est teli gendi optio cumque nihil impedit quo</p>
  <span class="more">READ MORE &gt;&gt;</span>
</article>
<article class="card abs" style="left:792px">
  <div class="card-photo abs" role="img" aria-label="Newly built custom home exterior" style="background:linear-gradient(180deg,#3e78c8 0%,#a9c4e2 45%,#d8d2c6 70%,#9a6a44 100%)"></div>
  <svg class="abs" style="left:8px;top:160px" width="298" height="40" viewBox="0 0 298 40" preserveAspectRatio="none"><path d="M0 0 Q149 50 298 0 L298 40 L0 40Z" fill="#fff"/><path d="M0 6 Q149 54 298 6 Q149 42 0 6Z" fill="#0d4fa3"/></svg>
  <h3>CUSTOM HOME BUILDING</h3>
  <p>Nam libero tempore, cum soluta nobis est teli gendi optio cumque nihil impedit quo</p>
  <span class="more">READ MORE &gt;&gt;</span>
</article>

<svg class="services abs" viewBox="0 0 1200 540" preserveAspectRatio="none">
  <defs><linearGradient id="band" x1="0" y1="0" x2="1" y2="1"><stop offset="0" stop-color="#0f4b9c"/><stop offset="1" stop-color="#1a5fb4"/></linearGradient></defs>
  <path d="M0 0 H1200 V500 Q600 430 0 500 Z" fill="url(#band)"/>
  <path d="M0 500 Q600 430 1200 500 V540 Q600 470 0 540 Z" fill="#6b9ad6"/>
  <path d="M0 525 Q600 455 1200 525 V540 Q600 475 0 540 Z" fill="#fff"/>
</svg>
<h2 class="section-title abs" style="top:1290px;color:#fff">OUR SERVICES</h2>

<div class="svc abs" style="left:80px">
  <div class="svc-ring"><svg width="80" height="80" viewBox="0 0 80 80"><path d="M40 10C20 10 8 26 10 44c2 16 18 26 30 24 6-1 4-8 8-10 5-2 12 2 16-4 6-10-4-44-24-44z" fill="#fff"/><circle cx="28" cy="30" r="5" fill="#1557ab"/><circle cx="42" cy="24" r="5" fill="#1557ab"/><circle cx="24" cy="46" r="5" fill="#1557ab"/><circle cx="36" cy="56" r="4" fill="#1557ab"/></svg></div>
  <h3>PAINTING</h3><p>Nam libero tempore, cum soluta nobis est teli gendi optio cumque nihil</p><span class="more">READ MORE &gt;&gt;</span>
</div>
<div class="svc abs" style="left:348px">
  <div class="svc-ring"><svg width="80" height="70" viewBox="0 0 80 70"><rect x="6" y="34" width="68" height="8" fill="#fff"/><path d="M10 42h60c0 12-8 18-20 18H30c-12 0-20-6-20-18z" fill="#fff"/><path d="M18 34V12a6 6 0 0 1 12 0" stroke="#fff" stroke-width="4" fill="none"/><circle cx="30" cy="18" r="4" fill="#fff"/></svg></div>
  <h3>BATHROOMS</h3><p>Nam libero tempore, cum soluta nobis est teli gendi optio cumque nihil</p><span class="more">READ MORE &gt;&gt;</span>
</div>
<div class="svc abs" style="left:616px">
  <div class="svc-ring"><svg width="80" height="70" viewBox="0 0 80 70"><rect x="8" y="8" width="24" height="18" fill="none" stroke="#fff" stroke-width="3"/><rect x="48" y="8" width="24" height="18" fill="none" stroke="#fff" stroke-width="3"/><rect x="6" y="36" width="68" height="26" fill="none" stroke="#fff" stroke-width="3"/><path d="M30 36v26M50 36v26" stroke="#fff" stroke-width="3"/><rect x="34" y="42" width="12" height="14" fill="#fff"/></svg></div>
  <h3>KITCHENS</h3><p>Nam libero tempore, cum soluta nobis est teli gendi optio cumque nihil</p><span class="more">READ MORE &gt;&gt;</span>
</div>
<div class="svc abs" style="left:884px">
  <div class="svc-ring"><svg width="70" height="80" viewBox="0 0 70 80"><path d="M14 8l36 30-12 14L14 32z" fill="#fff"/><path d="M30 44l-8 26h12l6-20z" fill="#fff"/><path d="M50 38l12 10" stroke="#fff" stroke-width="4"/></svg></div>
  <h3>DEMOLITION</h3><p>Nam libero tempore, cum soluta nobis est teli gendi optio cumque nihil</p><span class="more">READ MORE &gt;&gt;</span>
</div>

<h2 class="section-title abs" style="top:1802px">OUR BLOG</h2>

<article class="post abs" style="left:98px">
  <div class="post-photo" role="img" aria-label="Hands reviewing color swatches and plans" style="background:linear-gradient(135deg,#d9d4cc 0%,#b89a80 50%,#e8e4de 100%)"></div>
  <div class="date abs"><b>01</b><small>NOV</small></div>
  <h3>Finibus Bonorum et Malorum</h3>
  <p>Nam libero tempore, cum soluta nobis est eligendi optio cumque nihil impedit quo minus id quod maxim.</p>
  <div class="meta"><span>&#9679; John Doe</span><span>&#9675; 3 Comments</span></div>
</article>
<article class="post abs" style="left:442px">
  <div class="post-photo" role="img" aria-label="Carpenter working at a bench" style="background:linear-gradient(135deg,#e6e6e4 0%,#8a98a8 50%,#c9a37a 100%)"></div>
  <div class="date abs"><b>01</b><small>NOV</small></div>
  <h3>Finibus Bonorum et Malorum</h3>
  <p>Nam libero tempore, cum soluta nobis est eligendi optio cumque nihil impedit quo minus id quod maxim.</p>
  <div class="meta"><span>&#9679; John Doe</span><span>&#9675; 3 Comments</span></div>
</article>
<article class="post abs" style="left:786px">
  <div class="post-photo" role="img" aria-label="Couple reviewing plans in a framed house" style="background:linear-gradient(135deg,#c89a6a 0%,#e9dccb 50%,#8a5e3a 100%)"></div>
  <div class="date abs"><b>01</b><small>NOV</small></div>
  <h3>Finibus Bonorum et Malorum</h3>
  <p>Nam libero tempore, cum soluta nobis est eligendi optio cumque nihil impedit quo minus id quod maxim.</p>
  <div class="meta"><span>&#9679; John Doe</span><span>&#9675; 3 Comments</span></div>
</article>
<div class="rule abs"></div>

<h2 class="section-title abs" style="top:2342px">OUR GALLERY</h2>
<div class="gallery abs">
  <div role="img" aria-label="White kitchen with wood ceiling" style="background:linear-gradient(180deg,#7a4a2a 0%,#e8e4de 40%,#6a3a22 100%)"></div>
  <div role="img" aria-label="Bright bedroom with coffered ceiling" style="background:linear-gradient(180deg,#f2f0ec 0%,#d8cfc2 60%,#4a4038 100%)"></div>
  <div role="img" aria-label="Dark modern bathroom" style="background:linear-gradient(180deg,#e2e2e0 0%,#3a3432 55%,#6a6560 100%)"></div>
  <div role="img" aria-label="Light wood kitchen" style="background:linear-gradient(180deg,#eeeae4 0%,#b89672 60%,#8a6a4e 100%)"></div>
</div>
<div class="arrow abs" style="left:0"><svg width="10" height="16" viewBox="0 0 10 16"><path d="M8 2L2 8l6 6" stroke="#fff" stroke-width="2" fill="none"/></svg></div>
<div class="arrow abs" style="right:0"><svg width="10" height="16" viewBox="0 0 10 16"><path d="M2 2l6 6-6 6" stroke="#fff" stroke-width="2" fill="none"/></svg></div>

<footer>
  <div class="foot-brand abs">
    <div class="brand-box"></div>
    <div><div class="brand-name">Halvern Development</div><div class="brand-tag">CUSTOM HOMES • REMODELING</div></div>
  </div>
  <div class="foot-col abs" style="left:458px">
    <h4>Information</h4>
    <ul><li>Home</li><li>About Us</li><li>Services</li><li>Gallery</li><li>Blog</li><li>Contact Us</li></ul>
  </div>
  <div class="foot-col abs" style="left:620px">
    <h4>Newsletter Subscription</h4>
    <p>Register your Email Address to get<br>Information about us</p>
    <div class="field">Email Address</div>
    <div class="sub-btn">SUBSCRIBE</div>
  </div>
  <div class="foot-col abs" style="left:914px">
    <h4>Contact Us</h4>
    <div class="c-row"><svg width="12" height="16" viewBox="0 0 12 16"><path d="M6 0a6 6 0 0 1 6 6c0 4-6 10-6 10S0 10 0 6a6 6 0 0 1 6-6z" fill="#0d4fa3"/><circle cx="6" cy="6" r="2" fill="#fff"/></svg><span>42 Marlow st.<br>Fenwick , New Jersey</span></div>
    <div class="c-row"><svg width="14" height="14" viewBox="0 0 24 24"><path d="M6 2l4 4-2 3c1 3 4 6 7 7l3-2 4 4-3 4C10 22 2 14 2 5z" fill="#0d4fa3"/></svg><span>1 888 888 8888</span></div>
    <div class="c-row"><svg width="14" height="12" viewBox="0 0 24 18"><rect width="24" height="18" fill="#0d4fa3"/><path d="M1 1l11 9 11-9" fill="none" stroke="#fff" stroke-width="2"/></svg><span>info@halverndevelopment.com</span></div>
  </div>
  <div class="foot-rule abs"></div>
  <div class="copy abs">Copyrights © 2017, Halvern Development . All rights reserved.</div>
  <div class="social abs" style="left:1036px"></div>
  <div class="social abs" style="left:1076px"></div>
</footer>

</body>
</html>
```